MerrowtonPlatformKit Explainer

We are looking for an attractive/moderan info graphics that will explain our software and how it helps driving schools to fully integrated their business with clients and staff.
Attached word doc outlines the description of the main modules and most important services that our software performs.
The info graphic should be easy to read and understand as the main audience of school owners is not technically savvy and are generally averse to technology and computers.

Target Market(s)

Driving school owners and managers

Industry/Entity Type

Driving School

Font styles to use
Sans Serif

Colors

Designer to choose colors to be used in the design.

Requirements
Must have
• Clear graphics that complement logo colors. Easy to read understand.
Should not have
• complicated and confusing text.

```html
<!DOCTYPE html>
<html lang="en">
<head>
<meta charset="utf-8">
<title>MerrowtonPlatformKit Explainer</title>
<link rel="stylesheet" href="https://fonts.googleapis.com/css2?family=Open+Sans:wght@400;600;700;800&display=swap">
<style>
  :root{
    --blue:#1d4f91;
    --green:#5cb446;
    --coral:#f26b5b;
    --red:#e8523f;
    --yellow:#f7c04a;
    --amber:#f3a22b;
    --ink:#4a4a4a;
    --muted:#5f6368;
    --paper:#f7f7f7;
  }
  *{box-sizing:border-box;margin:0;padding:0}
  html,body{width:707px;height:1200px;overflow:hidden}
  body{background:var(--paper);font-family:"Open Sans",Arial,sans-serif;color:var(--ink);position:relative}

  .brand{position:absolute;top:26px;left:0;width:100%;display:flex;justify-content:center;align-items:center;gap:12px}
  .brand-dot{width:42px;height:42px;border-radius:50%;background:var(--blue)}
  .brand-name{font-size:27px;font-weight:700;color:var(--blue);letter-spacing:-.3px}

  .headline{position:absolute;top:100px;width:100%;text-align:center}
  .headline h1{font-size:22px;font-weight:700;color:var(--green);letter-spacing:-.2px}
  .headline h1 span{color:var(--blue);font-weight:400}
  .headline p{font-size:15.5px;color:var(--muted);line-height:1.45;margin-top:6px}

  .module{position:absolute;width:320px}
  .module h2{font-size:16px;font-weight:700;line-height:1.3;margin-bottom:8px}
  .module h2 b{font-weight:400;margin-right:4px}
  .module ul{padding-left:22px}
  .module li{font-size:10.6px;line-height:1.35;margin-bottom:2px;color:var(--ink)}
  .module li::marker{font-size:12px}

  .m-admin{top:206px;left:30px}
  .m-admin h2,.m-admin li::marker{color:var(--blue)}
  .m-web{top:206px;left:362px}
  .m-web h2,.m-web li::marker{color:var(--green)}
  .m-student{top:900px;left:30px;width:330px}
  .m-student h2,.m-student li::marker{color:var(--red)}
  .m-staff{top:900px;left:362px}
  .m-staff h2,.m-staff li::marker{color:var(--amber)}

  .steps{position:absolute;top:412px;left:0;width:707px;height:476px}
  .steps text{font-family:"Open Sans",Arial,sans-serif}
  .step-label{font-size:15px;font-weight:700;fill:#3c3c3c}
  .step-num{font-size:38px;font-weight:700;fill:#3c3c3c}
  .pill-text{font-size:12.5px;font-weight:700;fill:#fff}

  .features{position:absolute;left:0;bottom:0;width:100%;height:100px;background:var(--blue);color:#fff;padding:12px 30px 0}
  .features h3{text-align:center;font-size:16px;font-weight:700;letter-spacing:.3px;margin-bottom:9px}
  .features ul{display:grid;grid-template-columns:1fr 1fr;column-gap:24px;padding-left:14px}
  .features li{font-size:10.6px;line-height:1.4;margin-bottom:5px}
</style>
</head>
<body>

<header class="brand">
  <span class="brand-dot"></span>
  <span class="brand-name">MerrowtonPlatformKit</span>
</header>

<section class="headline">
  <h1>WEB BASED SOFTWARE DESIGNED <span>FOR DRIVING SCHOOLS</span></h1>
  <p>Each Modules Handles A Number Of Specific Features Functions<br>That Are Customizable For Each School</p>
</section>

<section class="module m-admin">
  <h2><b>01.</b>ADMINISTRATIVE:</h2>
  <ul>
    <li>All main administrative functions are accomplished.</li>
    <li>Admins can create student accounts, enroll them and manage student payments</li>
    <li>Create lessons and classroom</li>
    <li>Run business reports</li>
    <li>Create State Forms for compliance</li>
    <li>Schedule Student lessons and take classroom attendance</li>
    <li>Track vehicles via GPS and manage vehicle maintenance</li>
    <li>Send and receive text messages from students and parents</li>
  </ul>
</section>

<section class="module m-web">
  <h2><b>02.</b>WEBSITE ENROLLMENT</h2>
  <ul>
    <li>This module allows school to receive enrollments directly from their website and all information is saved directly into the schools database</li>
    <li>Website enrollments can also process credit card payments</li>
    <li>Student accounts are automatically created without any staff effort</li>
  </ul>
</section>

<svg class="steps" viewBox="0 18 707 476" role="img" aria-label="Four step module flow">
  <path d="M262 118 C 290 170, 360 150, 398 170" fill="none" stroke="var(--blue)" stroke-width="16"/>
  <path d="M330 150 C 360 150, 385 158, 400 172" fill="none" stroke="var(--green)" stroke-width="16"/>
  <path d="M410 244 C 390 290, 320 270, 275 292" fill="none" stroke="var(--green)" stroke-width="16"/>
  <path d="M340 272 C 310 276, 290 282, 274 294" fill="none" stroke="var(--coral)" stroke-width="16"/>
  <path d="M262 366 C 290 416, 360 398, 398 416" fill="none" stroke="var(--coral)" stroke-width="16"/>
  <path d="M330 398 C 360 398, 385 404, 400 418" fill="none" stroke="var(--yellow)" stroke-width="16"/>

  <rect x="250" y="42" width="296" height="62" rx="31" fill="var(--blue)"/>
  <text class="pill-text" x="305" y="78">ADMINISTRATIVE</text>
  <g fill="#fff" transform="translate(498 60)">
    <circle cx="8" cy="8" r="6"/><path d="M-2 28 a10 10 0 0 1 20 0z"/>
    <circle cx="22" cy="6" r="5" fill="none" stroke="#fff" stroke-width="3" stroke-dasharray="3 2"/>
  </g>

  <rect x="130" y="170" width="300" height="62" rx="31" fill="var(--green)"/>
  <text class="pill-text" x="186" y="206">WEBSITE ENROLLMENT</text>
  <g transform="translate(150 190)">
    <rect x="0" y="0" width="26" height="22" rx="2" fill="#fff"/>
    <rect x="3" y="6" width="20" height="2" fill="var(--green)"/>
    <rect x="3" y="11" width="14" height="2" fill="var(--green)"/>
    <rect x="3" y="16" width="17" height="2" fill="var(--green)"/>
  </g>

  <rect x="250" y="290" width="296" height="62" rx="31" fill="var(--coral)"/>
  <text class="pill-text" x="305" y="318">STUDENT AND</text>
  <text class="pill-text" x="305" y="334">PARENT CENTER</text>
  <g fill="#fff" transform="translate(490 308)">
    <path d="M0 10 L18 2 L36 10 L18 18z"/>
    <path d="M8 14 v9 q10 6 20 0 v-9 l-10 5z"/>
  </g>

  <rect x="130" y="416" width="300" height="62" rx="31" fill="var(--yellow)"/>
  <text class="pill-text" x="186" y="444">INSTRUCTOR AND STAFF</text>
  <text class="pill-text" x="196" y="460">SMART PHONE ACCESS</text>
  <g transform="translate(152 430)">
    <rect x="0" y="0" width="18" height="32" rx="3" fill="#fff"/>
    <rect x="3" y="4" width="12" height="20" fill="var(--yellow)"/>
    <circle cx="9" cy="28" r="1.8" fill="var(--yellow)"/>
  </g>

  <g>
    <circle cx="253" cy="72" r="44" fill="#fff" stroke="var(--blue)" stroke-width="10"/>
    <text class="step-label" x="253" y="58" text-anchor="middle">STEP</text>
    <text class="step-num" x="253" y="94" text-anchor="middle">01</text>
  </g>
  <g>
    <circle cx="424" cy="202" r="44" fill="#fff" stroke="var(--green)" stroke-width="10"/>
    <text class="step-label" x="424" y="188" text-anchor="middle">STEP</text>
    <text class="step-num" x="424" y="224" text-anchor="middle">02</text>
  </g>
  <g>
    <circle cx="253" cy="320" r="44" fill="#fff" stroke="var(--coral)" stroke-width="10"/>
    <text class="step-label" x="253" y="306" text-anchor="middle">STEP</text>
    <text class="step-num" x="253" y="342" text-anchor="middle">03</text>
  </g>
  <g>
    <circle cx="424" cy="446" r="40" fill="#fff" stroke="var(--yellow)" stroke-width="10"/>
    <text class="step-label" x="424" y="432" text-anchor="middle">STEP</text>
    <text class="step-num" x="424" y="468" text-anchor="middle">04</text>
  </g>
</svg>

<section class="module m-student">
  <h2><b>03.</b>STUDENT PARENT CENTER</h2>
  <ul>
    <li>Each student has the ability to access their own account and view status</li>
    <li>They can pay for any open balances</li>
    <li>They can purchase additional services</li>
    <li>They can schedule in-car lessons</li>
    <li>They can schedule classroom makeup session</li>
    <li>They can contact school</li>
    <li>They can access their account from any device anytime</li>
  </ul>
</section>

<section class="module m-staff">
  <h2><b>04.</b>INSTRUCTOR STAFF SMART PHONE ACCESS</h2>
  <ul>
    <li>Staff can and view their schedule in real time</li>
    <li>They can view students current program status</li>
    <li>They can complete lessons and take classroom attendance</li>
    <li>They can take electronic in-car evaluation</li>
    <li>Evaluation is sent in real-time to parent upon completion</li>
  </ul>
</section>

<footer class="features">
  <h3>AUTOMATIC FEATURES</h3>
  <ul>
    <li>Email notifications for in-car lessons and classroom session</li>
    <li>On-demand email notifications to individual parents/students</li>
    <li>Email notifications for new purchases and payments</li>
    <li>Text message reminders for in car and class lessons.</li>
  </ul>
</footer>

</body>
</html>
```